Flyer Design Project for psychologist

I need an A4 flyer designed for a new psychology practice I am setting up called Brightpath Haven. The focus is to cater for the mental health and well-being of mums throughout their life stages, to help them live their best life whilst providing support and guidance in their journey through Motherhood.
The flyer will be used to promote the main services we provide and will echo the look and feel of website (www.brightpathhaven.com.au) and logo design. Images/photos can be downloaded off the Brightpath Haven website homepage slider or on "Our Services" page.
Corporate colours
Colours:
Bright green: Pantone 376
Bright green as CMYK: c: 45.2% m: 0% y: 100% k: 0%
Logo text large grey: 70% black
Logo text strapline: 75% black
Tree: 80% black
Fonts:
Logo 'Brightpath Haven': Verdana
Logo 'Counselling & coaching services for mums': Gill Sans Light
Updates
OMG you are all awesome!!!! Will be very very hard decision :-(
Target Market(s)
Mothers - all life stages wanting support counselling
Industry/Entity Type
Mental Health
Look and feel
Each slider illustrates characteristics of the customer's brand and the style your logo design should communicate.

```html
<!DOCTYPE html>
<html lang="en">
<head>
<meta charset="utf-8">
<title>Brightpath Haven – Counselling &amp; Coaching for Mums</title>
<link href="https://fonts.googleapis.com/css2?family=Arimo:wght@400;700&family=Cabin:wght@400&family=Open+Sans:wght@700&display=swap" rel="stylesheet">
<style>
  :root {
    --green: #8cc63f;
    --grey-logo: #6d6e71;
    --grey-strap: #636466;
    --grey-band: #58595b;
    --grey-text: #4d4d4f;
    --white: #ffffff;
    --photo-a: #c9a58c;
    --photo-b: #6f5a4c;
  }
  html, body {
    margin: 0;
    padding: 0;
    width: 876px;
    height: 1200px;
    overflow: hidden;
    background: var(--white);
  }
  .flyer {
    position: relative;
    width: 876px;
    height: 1200px;
    background: var(--white);
    font-family: "Arimo", Arial, sans-serif;
    color: var(--grey-text);
    overflow: hidden;
  }
  .brand {
    position: absolute;
    left: 122px;
    top: 118px;
  }
  .brand__name {
    display: flex;
    align-items: center;
    gap: 22px;
    font-family: "Open Sans", Verdana, sans-serif;
    font-weight: 700;
    font-size: 60px;
    line-height: 1;
    letter-spacing: -1px;
    color: var(--grey-logo);
    margin: 0;
  }
  .brand__dot {
    width: 40px;
    height: 40px;
    border-radius: 50%;
    background: var(--grey-band);
  }
  .brand__strap {
    margin: 14px 0 0 2px;
    font-family: "Cabin", "Gill Sans", sans-serif;
    font-weight: 400;
    font-size: 34px;
    color: var(--grey-strap);
  }
  .photo {
    position: absolute;
    left: 0;
    top: 252px;
    width: 318px;
    height: 523px;
    background: linear-gradient(160deg, var(--photo-a) 0%, #b48a70 45%, var(--photo-b) 100%);
    border-top-right-radius: 140px;
  }
  .headline {
    position: absolute;
    left: 300px;
    top: 316px;
    margin: 0;
    font-weight: 700;
    color: var(--grey-logo);
  }
  .headline__lead {
    display: block;
    font-size: 50px;
    color: var(--green);
    line-height: 1.1;
  }
  .headline__lead small {
    font-size: 30px;
    font-weight: 400;
    color: var(--grey-logo);
  }
  .headline__line {
    display: block;
    font-size: 34px;
    line-height: 1.4;
  }
  .headline__line--indent {
    padding-left: 30px;
  }
  .headline__line--indent .accent { color: var(--green); }
  .headline__line--indent .soft { font-weight: 400; }
  .intro {
    position: absolute;
    left: 318px;
    right: 0;
    top: 458px;
    height: 316px;
    background: var(--green);
    color: var(--white);
    box-sizing: border-box;
    padding: 24px 30px 0 28px;
    font-size: 19.5px;
    line-height: 1.38;
    text-align: justify;
  }
  .intro p { margin: 0 0 24px; }
  .intro strong { font-weight: 700; }
  .services {
    position: absolute;
    left: 0;
    right: 0;
    top: 774px;
    height: 331px;
    background: var(--grey-band);
    color: var(--white);
  }
  .services__hearts {
    position: absolute;
    left: 70px;
    top: -10px;
    width: 130px;
    height: 200px;
    border-radius: 50px;
    background: linear-gradient(180deg, rgba(140,198,63,0.85), rgba(140,198,63,0.35));
  }
  .services__body {
    position: absolute;
    left: 240px;
    top: 20px;
  }
  .services__title {
    margin: 0 0 4px;
    font-size: 20px;
    font-weight: 700;
    color: var(--green);
  }
  .services__list {
    list-style: none;
    margin: 0;
    padding: 0;
    font-size: 19px;
    line-height: 22.5px;
  }
  .services__list li::before {
    content: "";
    display: inline-block;
    width: 7px;
    height: 7px;
    margin: 0 8px 3px 0;
    border-radius: 50%;
    background: var(--green);
  }
  .services__rebate {
    margin: 24px 0 0;
    font-size: 22px;
    font-weight: 700;
    color: var(--green);
  }
  .contact {
    position: absolute;
    left: 0;
    width: 830px;
    top: 1130px;
    text-align: center;
    font-size: 24px;
    line-height: 1.3;
    color: #222222;
  }
  .contact strong { font-size: 29px; font-weight: 700; }
</style>
</head>
<body>
<main class="flyer">
  <header class="brand">
    <h1 class="brand__name">Brightpath Haven<span class="brand__dot" aria-hidden="true"></span></h1>
    <p class="brand__strap">counselling &amp; coaching for mums</p>
  </header>

  <div class="photo" role="img" aria-label="Photo of a smiling mother hugging her young son"></div>

  <h2 class="headline">
    <span class="headline__lead">Live your best life <small>with</small></span>
    <span class="headline__line">Brightpath Haven Counselling</span>
    <span class="headline__line headline__line--indent"><span class="soft">and</span> <span class="accent">Coaching for Mums</span></span>
  </h2>

  <section class="intro">
    <p><strong>Brightpath Haven</strong> provides counselling and coaching services especially for mums. Our main focus is to help you effectively deal with the daily issues that you may face that impacts on your mental health and wellbeing whilst providing support and guidance in your journey through Motherhood.</p>
    <p>We help mums to uncover their strengths, set purposeful goals, develop the skills, ability and confidence that they need to be happier and lead meaningful and flourishing lives.</p>
  </section>

  <section class="services">
    <div class="services__hearts" role="img" aria-label="Green heart ornaments"></div>
    <div class="services__body">
      <h3 class="services__title">We can provide counselling and coaching for:</h3>
      <ul class="services__list">
        <li>Non-Directive Pregnancy Support</li>
        <li>Antenatal Depression</li>
        <li>Preparing for Baby</li>
        <li>Postnatal Depression</li>
        <li>Anxiety</li>
        <li>Motherhood Stress and Anger</li>
        <li>Surviving and Thriving Through a Breakup</li>
        <li>Work/Family Balance</li>
        <li>Increasing Happiness</li>
        <li>Finding Yourself in Motherhood.</li>
      </ul>
      <p class="services__rebate">Medicare rebates are available for some services</p>
    </div>
  </section>

  <footer class="contact">
    Call <strong>02 5550 4182</strong> to make an appointment<br>
    or visit <strong>www.brightpathhaven.com.au</strong>
  </footer>
</main>
</body>
</html>
```